Norvel Dispatch - Subscription Landing page

we need responsive landing page for a new news service about the Blockchain innovations coins and startups, the landing page includes vertical video player and call to action button, attach mockup.
temporary page
http://www.nvdp.io/
1 page

```html
<!DOCTYPE html>
<html lang="en">
<head>
<meta charset="utf-8">
<title>Norvel Dispatch — Be Ready for Tomorrow</title>
<link rel="stylesheet" href="https://fonts.googleapis.com/css2?family=Montserrat:wght@500;600;700&family=Outfit:wght@400;700&display=swap">
<style>
  :root {
    --navy-deep: #0d2350;
    --navy: #163a7a;
    --navy-light: #1f4f96;
    --blush: #f8eff0;
    --red: #e31e26;
    --red-dark: #c8141c;
    --white: #ffffff;
    --device: #e9e9ec;
    --device-edge: #d5d5da;
  }
  * { box-sizing: border-box; margin: 0; padding: 0; }
  html, body { width: 1200px; height: 677px; overflow: hidden; }
  body { font-family: "Outfit", "Montserrat", sans-serif; color: var(--white); }

  .landing {
    position: relative;
    width: 1200px; height: 677px;
    overflow: hidden;
    background: radial-gradient(ellipse at 75% 20%, var(--navy-light) 0%, var(--navy) 40%, var(--navy-deep) 100%);
  }
  .backdrop { position: absolute; inset: 0; }

  .brand {
    position: absolute; left: 174px; top: 40px;
    display: flex; align-items: center; gap: 12px;
  }
  .brand-dot { width: 40px; height: 40px; border-radius: 50%; background: var(--red); }
  .brand-name {
    font-family: "Outfit", sans-serif; font-weight: 700; font-size: 30px;
    color: var(--red); letter-spacing: -0.3px;
  }

  .intro { position: absolute; left: 172px; top: 150px; width: 320px; }
  .headline {
    font-family: "Montserrat", sans-serif; font-weight: 700;
    font-size: 40px; line-height: 44px; letter-spacing: -0.3px;
  }
  .lead {
    margin-top: 14px; font-family: "Montserrat", sans-serif; font-weight: 500;
    font-size: 16px; line-height: 24px;
  }
  .subscribe-note {
    margin-top: 30px; font-family: "Montserrat", sans-serif; font-weight: 600;
    font-size: 17px; line-height: 26px;
  }

  .cta { position: absolute; left: 171px; top: 422px; width: 228px; height: 54px; }
  .cta-ring {
    position: absolute; left: 0; top: 0; width: 221px; height: 54px;
    border: 1px solid var(--red); border-radius: 27px;
  }
  .cta-button {
    position: absolute; left: 24px; top: 4px; width: 204px; height: 46px;
    border-radius: 23px; background: var(--red);
    display: flex; align-items: center; justify-content: center;
    font-family: "Montserrat", sans-serif; font-weight: 700; font-size: 13px;
    letter-spacing: 0.3px; color: var(--white);
    box-shadow: 0 6px 14px rgba(0,0,0,0.25);
  }

  .channels { position: absolute; left: 173px; top: 512px; display: flex; gap: 7px; }
  .channel {
    width: 40px; height: 40px; border-radius: 50%;
    border: 1.5px solid var(--white);
    display: flex; align-items: center; justify-content: center;
    font-family: "Montserrat", sans-serif; font-weight: 600; font-size: 9px;
  }

  .device { position: absolute; left: 557px; top: 148px; width: 575px; height: 325px; }
  .device-lid {
    position: absolute; left: 46px; top: 0; width: 483px; height: 314px;
    background: var(--device); border-radius: 12px;
    box-shadow: 0 10px 30px rgba(0,0,0,0.25);
  }
  .video {
    position: absolute; left: 23px; top: 22px; width: 439px; height: 274px;
    background: linear-gradient(180deg, #a69c98 0%, #d99aa8 28%, #c98f86 55%, #3a3c4a 100%);
    display: flex; align-items: center; justify-content: center;
  }
  .device-base {
    position: absolute; left: 0; top: 313px; width: 575px; height: 11px;
    background: linear-gradient(180deg, #f2f2f4, var(--device-edge));
    border-radius: 0 0 40px 40px;
  }
</style>
</head>
<body>
<main class="landing">
  <svg class="backdrop" width="1200" height="677" viewBox="0 0 1200 677" aria-hidden="true">
    <path d="M200 677 Q 860 620 1070 310 Q 1160 170 1200 60 L1200 677 Z" fill="var(--blush)"/>
    <!-- play accents -->
    <g fill="var(--red)">
      <path d="M38 236 L62 249 L38 262 Z"/>
      <path d="M83 480 L94 486 L83 492 Z"/>
      <path d="M580 342 L557 354 L580 366 Z"/>
      <path d="M1144 396 L1162 406 L1144 416 Z"/>
      <path d="M727 530 L774 557 L727 584 Z"/>
      <path d="M1096 236 L1144 262 L1096 288 Z"/>
      <path d="M1178 213 L1183 216 L1178 219 Z"/>
    </g>
    <g fill="none" stroke="var(--red)" stroke-width="1.6">
      <path d="M628 122 L570 152 L628 178"/>
      <path d="M1086 248 L1154 290 L1086 330"/>
    </g>
  </svg>

  <header class="brand">
    <span class="brand-dot"></span>
    <span class="brand-name">Norvel Dispatch</span>
  </header>

  <section class="intro">
    <h1 class="headline">Be Ready for Tomorrow</h1>
    <p class="lead">Stay updated with all the latest blockchain innovations coins and startups in a daily video story.</p>
    <p class="subscribe-note">Subscribe for free in one of your channels below:</p>
  </section>

  <div class="cta">
    <span class="cta-ring"></span>
    <a class="cta-button" href="http://www.nvdp.io/">BROWSE NOTIFICATION</a>
  </div>

  <nav class="channels">
    <span class="channel">Loop</span>
    <span class="channel">Kite</span>
    <span class="channel">Pixa</span>
    <span class="channel">Reel</span>
    <span class="channel">Wire</span>
  </nav>

  <div class="device">
    <div class="device-lid">
      <div class="video" role="img" aria-label="Video presenter standing in front of a city skyline at dusk">
        <svg width="64" height="76" viewBox="0 0 64 76" aria-hidden="true">
          <path d="M10 4 Q4 0 4 8 L4 68 Q4 76 10 72 L60 42 Q64 38 60 34 Z" fill="var(--white)"/>
        </svg>
      </div>
    </div>
    <div class="device-base"></div>
  </div>
</main>
</body>
</html>
```